MRHT Needs Fundraiser Dinner Invite!!

The Marisol Hendrick Trust, a 501 3(c) non for profit has a yearly fundraiser, with varying themes. Last year it was "cowboys" and "cowgirls"
This year, it is Club Orchid, or 70's disco music. I have uploaded last years invite for reference, some stock photography for inspiration. You are not limited to using the stock photos.

Annual MRHT Fundraiser Dinner
October 13th, 2022
Starts: 6:30pm
RSVP By: September 20th
Place: The Bramwell
Price: $135 per ticket

Target Market(s)

Donors, Business People, Every person

Industry/Entity Type

Non for Profit

Font styles to use
Sans Serif

Colors
0054AA
0677BA
7BADD7
CADEEF
E8F1F8
E54698
E96AAD
F1A4CE
F9D9EA
FCEFF6
6B429C
8869AF
B7A5CE
E3DAEB
F3F0F8

Requirements
Must have
• The invite should be 5x7, be sophisticated as the clientele are mainly business people that come to support the cause. It should be fun and inviting at the same time.

```html
<!DOCTYPE html>
<html lang="en">
<head>
<meta charset="utf-8">
<title>Annual MRHT Fundraiser Dinner</title>
<link rel="stylesheet" href="https://fonts.googleapis.com/css2?family=Fraunces:opsz,wght,SOFT@9..144,900,100&family=Montserrat:wght@300;600;700&display=swap">
<style>
  :root {
    --navy: #0054AA;
    --blue: #0677BA;
    --sky: #7BADD7;
    --ice: #CADEEF;
    --pink: #E54698;
    --pink-mid: #E96AAD;
    --pink-soft: #F1A4CE;
    --pink-pale: #F9D9EA;
    --purple: #6B429C;
    --purple-mid: #8869AF;
    --lilac: #B7A5CE;
    --lilac-pale: #E3DAEB;
    --white: #FFFFFF;
    --floor: #E8E8EA;
    --peach: #F6DCC4;
    --coral: #EE6E86;
  }
  html, body { margin: 0; padding: 0; overflow: hidden; }
  body { width: 857px; height: 1200px; background: var(--white); }
  .invite {
    position: relative; width: 857px; height: 1200px; overflow: hidden;
    background:
      radial-gradient(circle at 50% 42%, var(--pink-pale) 0%, var(--pink-soft) 30%, transparent 55%),
      linear-gradient(160deg, var(--purple-mid) 0%, var(--pink-mid) 30%, var(--pink-soft) 55%, var(--pink-mid) 80%, var(--purple-mid) 100%);
  }
  .sunburst {
    position: absolute; inset: 0;
    background: radial-gradient(circle at 50% 45%, rgba(255,255,255,0.3), rgba(255,255,255,0) 60%);
  }
  .stage {
    position: absolute; left: 50%; top: 555px; width: 1500px; height: 1500px;
    margin-left: -750px; border-radius: 50%;
    background: radial-gradient(circle at 50% 8%, #F7F7F8 0%, var(--floor) 40%, #DCDCDF 100%);
  }
  .pearl { position: absolute; border-radius: 50%; }
  .pearl--white {
    left: 767px; top: 78px; width: 112px; height: 112px;
    background: radial-gradient(circle at 35% 30%, var(--white), #E4E4EA 55%, #B9B9C4 100%);
  }
  .pearl--pink {
    left: -12px; top: 622px; width: 118px; height: 118px;
    background: radial-gradient(circle at 40% 30%, var(--pink-pale), var(--pink-mid) 45%, var(--pink) 80%, #C42F7E 100%);
  }
  .disco-ball {
    position: absolute; left: 140px; top: 105px; width: 585px; height: 595px; border-radius: 50%;
    background:
      radial-gradient(circle at 62% 22%, rgba(202,222,239,0.9) 0%, rgba(202,222,239,0) 22%),
      radial-gradient(circle at 35% 82%, var(--peach) 0%, rgba(246,220,196,0) 35%),
      radial-gradient(circle at 50% 50%, #E7B6D8 0%, #D39ACB 50%, #B583C0 85%, #9C6DB2 100%);
    box-shadow: inset -18px -14px 40px rgba(107,66,156,0.25);
  }
  .title-banner { position: absolute; left: 70px; top: 268px; width: 720px; height: 210px; }
  .title {
    position: absolute; left: 70px; top: 300px; width: 680px; margin: 0;
    text-align: center; transform: rotate(-2deg);
    font-family: "Fraunces", Georgia, serif; font-weight: 900; font-variation-settings: "SOFT" 100;
    font-size: 60px; line-height: 76px; color: var(--white); letter-spacing: 0.5px;
  }
  .when {
    position: absolute; left: 0; top: 740px; width: 857px; margin: 0; text-align: center;
    font-family: "Fraunces", Georgia, serif; font-weight: 900; font-variation-settings: "SOFT" 100;
  }
  .when__date { display: block; font-size: 54px; line-height: 62px; color: var(--pink); text-shadow: -3px 3px 0 var(--blue); }
  .when__time { display: block; font-size: 54px; line-height: 62px; color: var(--navy); text-shadow: -3px 3px 0 var(--pink-mid); }
  .details {
    position: absolute; left: 135px; top: 882px; width: 583px; height: 150px; box-sizing: border-box;
    border: 2px solid var(--purple); border-radius: 26px;
    background: linear-gradient(90deg, var(--coral), var(--pink-mid) 50%, #A665B4);
    box-shadow: 0 6px 10px rgba(107,66,156,0.25);
    padding-top: 17px; text-align: center;
    font-family: "Montserrat", Arial, sans-serif; font-size: 28px; line-height: 38px;
    letter-spacing: 2.5px; color: var(--white); text-transform: uppercase;
  }
  .details__row { margin: 0; }
  .details__label { font-weight: 300; }
  .details__value { font-weight: 700; }
  .sparkle { position: absolute; width: 26px; height: 26px; }
  .sparkle--left { left: 145px; top: 907px; }
  .sparkle--right { left: 664px; top: 986px; }
  .footer-org {
    position: absolute; left: 160px; top: 1090px; width: 230px;
    font-family: "Montserrat", Arial, sans-serif; font-weight: 600; font-size: 20px; line-height: 26px; color: var(--purple-mid);
  }
  .footer-site {
    position: absolute; left: 435px; top: 1098px;
    display: flex; align-items: center; gap: 18px;
    font-family: "Montserrat", Arial, sans-serif; font-weight: 700; font-size: 34px; line-height: 44px; color: var(--purple-mid);
  }
  .footer-site__dot { width: 30px; height: 30px; border-radius: 50%; background: var(--lilac); }
</style>
</head>
<body>
<main class="invite">
  <div class="sunburst" role="img" aria-label="Swirling pink and purple sunburst rays"></div>
  <div class="stage" role="img" aria-label="Pale silver dance floor with scattered white light dots"></div>
  <div class="pearl pearl--white" role="img" aria-label="Glossy white pearl"></div>
  <div class="pearl pearl--pink" role="img" aria-label="Glossy pink pearl"></div>
  <div class="disco-ball" role="img" aria-label="Sparkling pink and lilac mirrored disco ball with glinting tiles"></div>

  <svg class="title-banner" viewBox="0 0 720 210" aria-hidden="true">
    <polygon points="70,50 590,16 620,34 690,36 682,160 696,186 630,182 100,206 62,170 14,160 26,118 44,104" fill="var(--pink-soft)"/>
    <polygon points="56,44 580,10 610,26 672,28 664,150 678,176 612,174 86,198 48,162 4,152 16,112 34,98" fill="var(--pink)"/>
    <polygon points="30,58 560,24 594,14 640,18 642,160 110,186 12,192 22,128" fill="var(--navy)"/>
  </svg>
  <h1 class="title">Annual MRHT<br>Fundraiser Dinner</h1>

  <p class="when">
    <span class="when__date">October 13th, 2022</span>
    <span class="when__time">Starts: 6:30pm</span>
  </p>

  <section class="details">
    <p class="details__row"><span class="details__label">RSVP By: </span><span class="details__value">September 20th</span></p>
    <p class="details__row"><span class="details__label">Place: </span><span class="details__value">The Bramwell</span></p>
    <p class="details__row"><span class="details__label">Price: </span><span class="details__value">$135 per ticket</span></p>
  </section>
  <svg class="sparkle sparkle--left" viewBox="0 0 24 24" aria-hidden="true"><path d="M12 0 L14 10 L24 12 L14 14 L12 24 L10 14 L0 12 L10 10 Z" fill="var(--white)"/></svg>
  <svg class="sparkle sparkle--right" viewBox="0 0 24 24" aria-hidden="true"><path d="M12 0 L14 10 L24 12 L14 14 L12 24 L10 14 L0 12 L10 10 Z" fill="var(--white)"/></svg>

  <div class="footer-org">The Marisol Hendrick Trust</div>
  <div class="footer-site"><span class="footer-site__dot"></span>MRHT.ORG</div>
</main>
</body>
</html>
```